Tulven Electrics Flyer Design Advertising

I am after an A5 Flyer design to help promote my electrical services business.
I would like to have information on what my business offers, photos of electrical work, and specials/deals for an amount of time.

Industry/Entity Type

Electrician

Font styles to use
Sans Serif

Colors
0292cd
33a6d7
85cae6
3176b5
333333
1b1b1b
ffffff
5c5c5c
474747

Requirements
Must have
• Specialising in New homes, renovations and commercial projects
• Contact details:
• ph. 0437 619 458
• email admin@tulvenelectrics.example.au
• facebook TulvenElectrics
• Specials/Deals:
• 10% off all electrical services
• or
• Free LED downlights on installation
• *Terms conditions apply
• ALL RESIDENTIAL & COMMERCIAL ELECTRICAL SERVICES
• - New Home installations
• - Commercial projects
• - Shop fit outs
• - Renovations
• - Smoke Detectors
• - Air Conditioning and Ceiling Fans
• - Garden Lighting
• - Oven and Cooktop Installations
• - Power Point installation
• - LED lighting upgrades
• - Security Lighting
• - Switchboard upgrades
• - Test and Tag
• - Commercial Property
• - General Electrical Maintenance

```html
<!DOCTYPE html>
<html lang="en">
<head>
<meta charset="utf-8">
<title>Tulven Electrics Flyer</title>
<link rel="stylesheet" href="https://fonts.googleapis.com/css2?family=Fira+Sans:ital,wght@0,600;1,400;1,600;1,700&family=Open+Sans:wght@400;600;700&display=swap">
<style>
  :root {
    --sky: #4dd8fa;
    --paper: #e6e7e9;
    --charcoal: #333333;
    --ink: #1b1b1b;
    --slate: #5c5c5c;
    --teal-panel: #608c90;
    --teal-band-a: #5b95a2;
    --teal-band-b: #6cc3d6;
    --hex-icon: #5fd0f2;
    --white: #ffffff;
  }
  * { box-sizing: border-box; margin: 0; padding: 0; }
  html, body { width: 846px; height: 1200px; overflow: hidden; background: var(--white); }
  .flyer {
    position: relative; width: 846px; height: 1200px; overflow: hidden;
    background: var(--sky); border: 1px solid var(--ink);
    font-family: "Open Sans", sans-serif; color: var(--charcoal);
  }
  .abs { position: absolute; }
  .backdrop { left: 0; top: 0; }

  .brand-mark { left: 26px; top: 18px; width: 150px; height: 150px; border-radius: 50%; background: #3c4246; }
  .brand-name {
    left: 186px; top: 72px; font-family: "Open Sans", sans-serif; font-weight: 700;
    font-size: 34px; color: var(--charcoal); white-space: nowrap; letter-spacing: 0.5px;
  }
  .licence { left: 26px; top: 182px; font-size: 12.5px; font-weight: 600; line-height: 16px; color: var(--charcoal); }

  .sector-label {
    font-family: "Open Sans", sans-serif; font-weight: 700; font-size: 22px; color: var(--charcoal);
    transform: rotate(-8.5deg); transform-origin: center; white-space: nowrap;
    width: 160px; text-align: center; margin-left: -80px;
  }

  .tagline-band {
    left: 12px; top: 551px; width: 690px; height: 90px;
    background: linear-gradient(90deg, var(--teal-band-a), var(--teal-band-b));
  }
  .tagline {
    left: 26px; top: 556px; font-family: "Fira Sans", sans-serif; font-style: italic; font-weight: 600;
    font-size: 29px; line-height: 40px; color: var(--white);
  }

  .deals-ring { left: 619px; top: 429px; width: 208px; height: 208px; border-radius: 50%;
    background: radial-gradient(circle, #7a8588 55%, #4c5457 100%); }
  .deals-disc { left: 632px; top: 442px; width: 182px; height: 182px; border-radius: 50%; background: var(--white);
    text-align: center; color: var(--charcoal); }
  .deals-title { margin-top: 20px; font-family: "Fira Sans", sans-serif; font-style: italic; font-weight: 700;
    font-size: 15px; text-decoration: underline; color: var(--ink); }
  .deals-line { font-size: 13.5px; line-height: 18px; }
  .deals-or { display: block; margin: 2px auto 0; }
  .deals-terms { font-size: 6px; margin-top: 5px; }

  .services-heading {
    left: 0; width: 846px; top: 683px; text-align: center; font-family: "Fira Sans", sans-serif;
    font-style: italic; font-weight: 600; font-size: 30.5px; color: var(--white);
    text-decoration: underline; text-decoration-thickness: 2px; text-underline-offset: 4px; white-space: nowrap;
  }

  .services-panel { left: 23px; top: 751px; width: 800px; height: 288px; background: var(--teal-panel); }
  .notch { width: 48px; height: 48px; border-radius: 50%; background: var(--sky); }
  .notch-tl { left: -1px; top: 727px; }
  .notch-br { left: 799px; top: 1015px; }
  .service-list { list-style: none; text-align: center; color: var(--white); font-weight: 600;
    font-size: 20px; line-height: 31px; white-space: nowrap; }
  .list-left { left: 23px; width: 380px; top: 764px; }
  .list-right { left: 447px; width: 380px; top: 767px; }
  .list-wide { left: 23px; width: 800px; top: 989px; }

  .contact-title { left: 0; width: 846px; top: 1092px; text-align: center; font-family: "Fira Sans", sans-serif;
    font-style: italic; font-weight: 700; font-size: 37px; color: var(--ink); text-decoration: underline;
    text-decoration-thickness: 2px; text-underline-offset: 4px; }
  .contact-row { left: 0; width: 846px; top: 1152px; display: flex; justify-content: center; align-items: center;
    gap: 14px; font-family: "Fira Sans", sans-serif; font-style: italic; font-size: 21px; color: var(--ink); white-space: nowrap; }
  .contact-item { display: flex; align-items: center; gap: 7px; }
  .divider { width: 5px; height: 16px; background: var(--ink); }
  .social-square { width: 17px; height: 17px; background: #6ab5d8; border-radius: 2px; }
</style>
</head>
<body>
<div class="flyer">
  <svg class="abs backdrop" width="846" height="1200" viewBox="0 0 846 1200">
    <defs>
      <linearGradient id="g-pool" x1="0" y1="0" x2="0" y2="1"><stop offset="0" stop-color="#6b7a5c"/><stop offset=".5" stop-color="#8a6a3c"/><stop offset="1" stop-color="#1f3a2e"/></linearGradient>
      <linearGradient id="g-kitchen" x1="0" y1="0" x2="1" y2="1"><stop offset="0" stop-color="#d9dbdc"/><stop offset=".5" stop-color="#4a4d50"/><stop offset="1" stop-color="#eeeeee"/></linearGradient>
      <linearGradient id="g-patio" x1="0" y1="0" x2="0" y2="1"><stop offset="0" stop-color="#3c4a3a"/><stop offset=".5" stop-color="#c9a06a"/><stop offset="1" stop-color="#4a3a2c"/></linearGradient>
      <linearGradient id="g-lounge" x1="0" y1="0" x2="1" y2="0"><stop offset="0" stop-color="#f1f1ef"/><stop offset=".6" stop-color="#b7c7a8"/><stop offset="1" stop-color="#e6e6e3"/></linearGradient>
      <linearGradient id="g-dining" x1="0" y1="0" x2="1" y2="1"><stop offset="0" stop-color="#3a3a3c"/><stop offset=".5" stop-color="#e9e6df"/><stop offset="1" stop-color="#8a7a66"/></linearGradient>
      <linearGradient id="g-bath" x1="0" y1="0" x2="1" y2="1"><stop offset="0" stop-color="#eef0f1"/><stop offset=".6" stop-color="#d6dadb"/><stop offset="1" stop-color="#9aa3a6"/></linearGradient>
      <linearGradient id="g-living" x1="0" y1="0" x2="1" y2="1"><stop offset="0" stop-color="#d8524a"/><stop offset=".4" stop-color="#f0f0ee"/><stop offset="1" stop-color="#c9ccc9"/></linearGradient>
    </defs>
    <polygon points="0,0 846,0 846,118 0,244" fill="var(--paper)"/>
    <polygon points="0,244 846,118 846,154 0,280" fill="var(--charcoal)"/>

    <g transform="translate(486 101)">
      <polygon points="0,-32 28,-16 28,16 0,32 -28,16 -28,-16" fill="var(--hex-icon)"/>
      <path d="M-15,4 L0,-10 L15,4 M-11,1 V14 H11 V1" fill="none" stroke="var(--charcoal)" stroke-width="2.5"/>
      <rect x="-3" y="5" width="6" height="9" fill="var(--charcoal)"/>
    </g>
    <g transform="translate(634 81)">
      <polygon points="0,-32 28,-16 28,16 0,32 -28,16 -28,-16" fill="var(--hex-icon)"/>
      <rect x="-14" y="-6" width="10" height="20" fill="var(--charcoal)"/>
      <rect x="-3" y="-14" width="10" height="28" fill="var(--charcoal)"/>
      <rect x="8" y="-2" width="8" height="16" fill="var(--charcoal)"/>
    </g>
    <g transform="translate(767 63)">
      <polygon points="0,-32 28,-16 28,16 0,32 -28,16 -28,-16" fill="var(--hex-icon)"/>
      <path d="M-16,14 V-2 L-6,4 V-2 L4,4 V-2 L16,4 V14 Z" fill="var(--charcoal)"/>
      <rect x="-14" y="-14" width="5" height="14" fill="var(--charcoal)"/>
    </g>

    <g stroke="var(--white)" stroke-width="4" stroke-linejoin="round">
      <g role="img" aria-label="Photo: modern home with lit pool at dusk"><polygon points="600,195 715,223 715,295 600,323 485,295 485,223" fill="url(#g-pool)"/></g>
      <g role="img" aria-label="Photo: dark modern kitchen with pendant lights"><polygon points="246,296 363,324 363,397 246,425 130,397 130,324" fill="url(#g-kitchen)"/></g>
      <g role="img" aria-label="Photo: outdoor patio with wall lights"><polygon points="482,296 598,324 598,397 482,425 367,397 367,324" fill="url(#g-patio)"/></g>
      <g role="img" aria-label="Photo: bright living room with air conditioner"><polygon points="718,296 835,324 835,397 718,425 602,397 602,324" fill="url(#g-lounge)"/></g>
      <g role="img" aria-label="Photo: kitchen and dining area with pendant lights"><polygon points="127,398 244,426 244,500 127,528 11,500 11,426" fill="url(#g-dining)"/></g>
      <g role="img" aria-label="Photo: white bathroom with lighting"><polygon points="364,398 482,426 482,500 364,528 246,500 246,426" fill="url(#g-bath)"/></g>
      <g role="img" aria-label="Photo: living room with ceiling fan and artwork"><polygon points="601,398 717,426 717,500 601,528 485,500 485,426" fill="url(#g-living)"/></g>
    </g>
  </svg>

  <div class="abs brand-mark"></div>
  <div class="abs brand-name">Tulven Electrics</div>
  <div class="abs licence">Lic no. 51308<br>ABN 48 903 217 665</div>

  <div class="abs sector-label" style="left:486px; top:138px;">Residential</div>
  <div class="abs sector-label" style="left:634px; top:117px;">Commercial</div>
  <div class="abs sector-label" style="left:767px; top:99px;">Industrial</div>

  <div class="abs tagline-band"></div>
  <div class="abs tagline">Specialising In New<br>Homes, Renovations And Commercial Projects</div>

  <div class="abs deals-ring"></div>
  <div class="abs deals-disc">
    <div class="deals-title">Specials/Deals:</div>
    <div class="deals-line" style="margin-top:4px;">10% off all<br>electrical services</div>
    <svg class="deals-or" width="40" height="30" viewBox="0 0 40 30">
      <polygon points="6,2 30,2 24,12 36,12 14,30 18,17 4,17" fill="var(--ink)"/>
      <text x="20" y="15" text-anchor="middle" font-family="Open Sans, sans-serif" font-weight="700" font-size="11" fill="var(--white)">or</text>
    </svg>
    <div class="deals-line">Free LED downlights<br>on installation</div>
    <div class="deals-terms">*Terms conditions apply</div>
  </div>

  <div class="abs services-heading">ALL RESIDENTIAL &amp; COMMERCIAL ELECTRICAL SERVICES</div>

  <div class="abs services-panel"></div>
  <div class="abs notch notch-tl"></div>
  <div class="abs notch notch-br"></div>
  <ul class="abs service-list list-left">
    <li>New Home installations</li>
    <li>Commercial projects</li>
    <li>Shop fit outs</li>
    <li>Renovations</li>
    <li>Smoke Detectors</li>
    <li>Garden Lighting</li>
    <li>Oven and Cooktop Installations</li>
  </ul>
  <ul class="abs service-list list-right">
    <li>Power Point installation</li>
    <li>LED lighting upgrades</li>
    <li>Security Lighting</li>
    <li>Switchboard upgrades</li>
    <li>Test and Tag</li>
    <li>Commercial Property</li>
    <li>General Electrical Maintenance</li>
  </ul>
  <ul class="abs service-list list-wide">
    <li>Air Conditioning and Ceiling Fans</li>
  </ul>

  <div class="abs contact-title">Contact Details:</div>
  <div class="abs contact-row">
    <span class="contact-item">
      <svg width="20" height="20" viewBox="0 0 20 20"><circle cx="10" cy="10" r="8.5" fill="none" stroke="#7ab8d6" stroke-width="1.5"/><path d="M6.5,5.5 C6,9 10,14 14,13.5 L14,11.8 L12,11 L11,12 C9.5,11.3 8.5,10.2 8,8.8 L9,7.8 L8.2,5.6 Z" fill="#7ab8d6"/></svg>
      0437 619 458
    </span>
    <span class="divider"></span>
    <span class="contact-item">
      <svg width="20" height="18" viewBox="0 0 20 18"><path d="M2,7 L10,1 L18,7 V17 H2 Z" fill="none" stroke="#7ab8d6" stroke-width="1.5"/><path d="M2,7 L10,12 L18,7" fill="none" stroke="#7ab8d6" stroke-width="1.5"/></svg>
      admin@tulvenelectrics.example.au
    </span>
    <span class="divider"></span>
    <span class="contact-item">
      <span class="social-square"></span>
      TulvenElectrics
    </span>
  </div>
</div>
</body>
</html>
```